Homemaking training schools needs a Business Card design

Designer, Hello!

No special requirements, good-looking enough.
--------------------------------------------------------------------------

Name: Martin Liao
Chairman
Tel: 0574-61947352
Mobile: 13857204619
Email: kelvow@mailbrook.example
Web: www.pkt2019.example
Add: No.288, LanfengJie, QiaoyuQu, Ningbo, Zhejiang

LOGO
Ningbo PKT Homemaking Training School

Target Market(s)

pregnant women, mothers, infants, the elderly and families, including cleaning, cooking, nursing training.

Industry/Entity Type

Business

Contact Information for Business Card

Name: Martin Liao
Chairman
Tel: 0574-61947352
Mobile: 13857204619
Email: kelvow@mailbrook.example
Web: www.pkt2019.example

LOGO

Font styles to use
Serif
Sans Serif
Decorative

Requirements
Nice to have
• Feels: clean, specifications, safety, comfort, warmth and happiness.

```html
<!DOCTYPE html>
<html lang="en">
<head>
<meta charset="utf-8">
<title>PeiKangTang Business Card</title>
<link rel="stylesheet" href="https://fonts.googleapis.com/css2?family=Montserrat:wght@400;500;600&display=swap">
<style>
  :root {
    --bg: #cde8df;
    --card: #ffffff;
    --blue: #0a7cc2;
    --blue-deep: #1467b3;
    --pink: #e3168c;
    --ink-light: #ffffff;
  }
  * { box-sizing: border-box; margin: 0; padding: 0; }
  html, body { width: 1200px; height: 856px; overflow: hidden; }
  body {
    background: var(--bg);
    font-family: "Montserrat", sans-serif;
    display: flex;
    align-items: center;
    justify-content: center;
    gap: 40px;
  }
  .card {
    position: relative;
    width: 540px;
    height: 310px;
    background: var(--card);
    border-radius: 26px;
    overflow: hidden;
    box-shadow: 0 10px 24px rgba(40, 90, 80, 0.18);
  }
  .brand {
    display: flex;
    align-items: center;
    gap: 8px;
    color: var(--blue-deep);
    font-weight: 600;
    font-size: 28px;
    letter-spacing: 0.5px;
    white-space: nowrap;
  }
  .brand-dot {
    width: 12px; height: 12px;
    border-radius: 50%;
    background: var(--pink);
  }

  /* Front */
  .front .brand { position: absolute; top: 40px; right: 34px; font-size: 25px; }
  .holder { position: absolute; top: 108px; left: 40px; color: var(--blue); }
  .holder-name { font-size: 24px; font-weight: 400; letter-spacing: 1px; text-transform: uppercase; }
  .holder-title { font-size: 17px; font-weight: 400; margin-top: 2px; }
  .rule { position: absolute; left: 0; right: 0; top: 168px; height: 4px; background: var(--blue-deep); }
  .band {
    position: absolute; left: 0; right: 0; top: 178px; bottom: 0;
    background: var(--blue);
    color: var(--ink-light);
    display: flex;
    align-items: center;
    padding: 0 26px 0 20px;
  }
  .contacts { list-style: none; flex: 0 0 290px; display: flex; flex-direction: column; gap: 6px; }
  .contacts li { display: flex; justify-content: flex-end; align-items: center; gap: 10px; font-size: 14px; white-space: nowrap; }
  .contacts svg { width: 16px; height: 16px; flex: none; }
  .divider { width: 1px; height: 78px; background: rgba(255,255,255,0.8); margin: 0 22px; }
  .address { font-style: normal; font-size: 14px; line-height: 1.4; }

  /* Back */
  .back .brand { position: absolute; left: 50%; top: 46%; transform: translate(-50%, -50%); }
  .back-rule { position: absolute; left: 0; right: 0; bottom: 44px; height: 4px; background: var(--blue-deep); }
  .back-band { position: absolute; left: 0; right: 0; bottom: 0; height: 36px; background: var(--blue); }
  .back-accent { position: absolute; left: 0; top: 0; width: 100%; height: 6px; background: var(--pink); }
</style>
</head>
<body>
  <section class="card front" aria-label="Card front">
    <div class="brand"><span class="brand-dot"></span>PeiKangTang</div>
    <div class="holder">
      <div class="holder-name">Martin Liao</div>
      <div class="holder-title">Chairman</div>
    </div>
    <div class="rule"></div>
    <div class="band">
      <ul class="contacts">
        <li>0574-61947352
          <svg viewBox="0 0 16 16" fill="none" stroke="#fff" stroke-width="1.2"><circle cx="8" cy="8" r="7"/><path d="M5.5 4.5l1.5 1.5-1 1c.6 1.2 1.3 1.9 2.5 2.5l1-1 1.5 1.5-1 1c-2.5-.5-4.5-2.5-5-5z"/></svg></li>
        <li>13857204619
          <svg viewBox="0 0 16 16" fill="none" stroke="#fff" stroke-width="1.2"><circle cx="8" cy="8" r="7"/><rect x="5.5" y="3.5" width="5" height="9" rx="1"/></svg></li>
        <li>kelvow@mailbrook.example
          <svg viewBox="0 0 16 16" fill="none" stroke="#fff" stroke-width="1.2"><rect x="1.5" y="3.5" width="13" height="9"/><path d="M1.5 3.5l6.5 5 6.5-5M1.5 12.5l5-4.5M14.5 12.5l-5-4.5"/></svg></li>
        <li>www.pkt2019.example
          <svg viewBox="0 0 16 16" fill="none" stroke="#fff" stroke-width="1.2"><circle cx="8" cy="8" r="7"/><path d="M1 8h14M8 1c-3 3.5-3 10.5 0 14M8 1c3 3.5 3 10.5 0 14"/></svg></li>
      </ul>
      <div class="divider"></div>
      <address class="address">No.288, LanfengJie,<br>QiaoyuQu, Ningbo<br>Zhejiang</address>
    </div>
  </section>

  <section class="card back" aria-label="Card back">
    <span class="back-accent"></span>
    <div class="brand"><span class="brand-dot"></span>PeiKangTang</div>
    <span class="back-rule"></span>
    <span class="back-band"></span>
  </section>
</body>
</html>
```